Carers Beyond Borders Guild Business Cards

The Carers Beyond Borders Guild provides Continuing Professional Development opportunities to Nurses both online and via exciting Travel adventures to fabulous destinations worldwide.

We require business cards for our staff and at a minimum, the card will need:

Full Name
Position
p 07 5282 6917
m 0400 000 000 (optional)
e info@wardlinkalliance.com.au
w www.wardlinkalliance.com.au

I will need a template so that I can edit different employee details as they come and go.

Here is our website - www.wardlinkalliance.com.au, so you can see what we are about.

I have attached our logo and if you need to know these are the colours we use on our website - orange #F4701D, Purple #6A136A and green #63AB32

Let me know if you need further details, I look forward to seeing your designs.

Cheers,
Maria.

```html
<!DOCTYPE html>
<html lang="en">
<head>
<meta charset="utf-8">
<title>Carers Beyond Borders Guild – Business Cards</title>
<link href="https://fonts.googleapis.com/css2?family=Questrial&display=swap" rel="stylesheet">
<style>
  :root {
    --orange: #F4701D;
    --card-orange: #F28124;
    --purple: #6A1F7A;
    --white: #FFFFFF;
    --backdrop: #3A3A3A;
    --divider: #8A4A96;
  }
  * { margin: 0; padding: 0; box-sizing: border-box; }
  html, body {
    width: 1200px; height: 900px; overflow: hidden;
    background: var(--backdrop);
    font-family: "Questrial", "Century Gothic", sans-serif;
  }
  .canvas { position: relative; width: 1200px; height: 900px; }

  .card {
    position: absolute; width: 580px; height: 354px;
    box-shadow: 0 8px 24px rgba(0,0,0,0.35);
  }
  .card--front { left: 540px; top: 70px; background: var(--card-orange); }
  .card--back  { left: 80px;  top: 470px; background: var(--white); }

  .wordmark {
    display: flex; align-items: center; gap: 16px;
    position: absolute; line-height: 0.95; letter-spacing: 0.5px;
  }
  .wordmark__dot { width: 34px; height: 34px; border-radius: 50%; flex: none; }
  .wordmark__name { font-size: 30px; }

  .card--front .wordmark { left: 170px; top: 122px; color: var(--white); }
  .card--front .wordmark__dot { background: var(--white); }

  .card--back .wordmark { left: 36px; top: 104px; color: var(--purple); }
  .card--back .wordmark__dot { background: var(--purple); }
  .card--back .wordmark__name { font-size: 27px; }

  .divider {
    position: absolute; left: 292px; top: 96px;
    width: 2px; height: 160px; background: var(--divider);
  }

  .contact { position: absolute; left: 312px; top: 92px; color: var(--purple); }
  .contact__name { font-size: 25px; font-weight: 700; letter-spacing: 0.3px; }
  .contact__role { font-size: 16px; color: var(--orange); margin-bottom: 12px; }
  .contact__list { list-style: none; }
  .contact__item {
    display: flex; align-items: center; gap: 8px;
    font-size: 14.5px; margin-bottom: 6px;
  }
  .contact__item--bare { padding-left: 26px; }
  .icon { width: 18px; height: 18px; flex: none; }
</style>
</head>
<body>
<main class="canvas">

  <section class="card card--front" aria-label="Card front">
    <div class="wordmark">
      <span class="wordmark__dot"></span>
      <span class="wordmark__name">carers<br>beyond borders<br>guild</span>
    </div>
  </section>

  <section class="card card--back" aria-label="Card back">
    <div class="wordmark">
      <span class="wordmark__dot"></span>
      <span class="wordmark__name">carers<br>beyond<br>borders<br>guild</span>
    </div>

    <div class="divider"></div>

    <div class="contact">
      <p class="contact__name">Daniel Reyes</p>
      <p class="contact__role">Managing director</p>
      <ul class="contact__list">
        <li class="contact__item">
          <svg class="icon" viewBox="0 0 18 18" aria-hidden="true"><circle cx="9" cy="9" r="9" fill="var(--purple)"/><path d="M5 7c0-1 1-2 4-2s4 1 4 2l-1.5 1L10 7H8L6.5 8z M6 10h6v3H6z" fill="#fff"/></svg>
          <span>07 5282 6917</span>
        </li>
        <li class="contact__item">
          <svg class="icon" viewBox="0 0 18 18" aria-hidden="true"><circle cx="9" cy="9" r="9" fill="var(--purple)"/><rect x="6.5" y="4" width="5" height="10" rx="1" fill="#fff"/><rect x="7.5" y="5.5" width="3" height="5" fill="var(--purple)"/></svg>
          <span>0400 000 000</span>
        </li>
        <li class="contact__item">
          <svg class="icon" viewBox="0 0 18 18" aria-hidden="true"><circle cx="9" cy="9" r="9" fill="var(--purple)"/><rect x="4.5" y="6" width="9" height="6.5" fill="#fff"/><path d="M4.5 6l4.5 4 4.5-4" stroke="var(--purple)" stroke-width="1" fill="none"/></svg>
          <span>info@wardlinkalliance.com.au</span>
        </li>
        <li class="contact__item">
          <svg class="icon" viewBox="0 0 18 18" aria-hidden="true"><circle cx="9" cy="9" r="9" fill="var(--purple)"/><circle cx="9" cy="9" r="5" fill="none" stroke="#fff" stroke-width="1.2"/><path d="M4 9h10M9 4c-2 3-2 7 0 10M9 4c2 3 2 7 0 10" stroke="#fff" stroke-width="1" fill="none"/></svg>
          <span>www.wardlinkalliance.com.au</span>
        </li>
      </ul>
    </div>
  </section>

</main>
</body>
</html>
```